Designing A poster for a zany musical comedy slated for an Off-Broadway run!

We need a poster design for a musical comedy that is scheduled in theatres around the U.S. The poster needs to capture the audacious and crazy nature of this cutting edge musical where 7 actors play everyone in the town, men, women and children. The show is funny, political, satirical, absurd and controversial.
Synopsis:A new campy, cheeky, audacious musical comedy. The ladies of the Pelloway Third Gospel Chapel Ladies’ Helping Circle are getting together to produce their annual Harvest Bonnet Jubilee. Six actors play every character in this singing, acting, dancing, improv tour de force. As the ‘Steeple Sisters’ prepare for their pageant, chaos and calamity bring out less than ‘saintly’ behavior. The result is Heaven sent hilarity!

A review to give you an idea: “It’s hoot. Actually, that is too mild a word. At its heart, this is a showcase for six journeymen actors (and one musician) to strut their prodigious talents…The result is like the funnyman’s version of an VKTR highlight reel – nonstop humor from first-rate pros. When they turn their attention to the serious business of humor – to primping and eyelash-batting, to hip-wiggling, to catty banter, to the deliciously clever maze of men playing women who are mocking men – it’s a ball.”—Review by Warren Pickett, Dayton Ledger-Post, 2010--

Target Market(s)

Broadway and Theatre audiences

Industry/Entity Type

Entertainment Industry

Logo Text

STEEPLE SISTERS, the musical

Colors

Designer to choose colors to be used in the design.

Requirements
Must have
• It must have the title: STEEPLE SISTERS
• It should the subtitle: The Musical
• It must have the following credits:
• Book and Story by Hal Brody
• Music by Toby Kessler, Lyrics by Marla Brody
• Additional Material by Fenwick Ashby
Nice to have
• It should have a sense of humor. Attached are images of the characters in the town of Pelloway, U.S.A. Use these images if you like. Not the photographic image but maybe caricatures of the images. Maybe cartoon or stylized?
• It should have a sense of humor. Attached are images of the characters in the town of Pelloway, U.S.A. Use these images to create caricatures. Not the photographic image but maybe caricatures of the images. Maybe cartoon or stylized? Or perhaps stay away from people and feature a church... with a toppled steeple... or a tilted steeple. Or maybe the characters peeking out through the windows of the church...
Should not have
• Do not use the photographs. Instead more graphic designed or illustrated.The photographs provided are just for reference. Do not put these in the design! You can use them to create caricatures or cartoon versions of the people. But do not just cut and paste the photos. Instead more graphic designed or illustrated.

```html
<!DOCTYPE html>
<html lang="en">
<head>
<meta charset="utf-8">
<title>Steeple Sisters – the Musical</title>
<link rel="stylesheet" href="https://fonts.googleapis.com/css2?family=Yellowtail&family=Oswald:wght@300;400&display=swap">
<style>
  :root {
    --page: #e9e8e6;
    --poster-top: #4c3b36;
    --poster-bottom: #3a2d2b;
    --title: #f3796a;
    --credit: #a89a94;
    --credit-name: #cfc3bd;
    --coral: #f46f62;
    --yellow: #fbb94a;
    --orange: #f2661f;
    --magenta: #f23b6a;
    --rose: #ee706d;
    --purple: #9a6c9e;
    --green: #3fa57b;
  }
  * { margin: 0; padding: 0; box-sizing: border-box; }
  html, body {
    width: 1200px;
    height: 1148px;
    overflow: hidden;
    background: var(--page);
  }
  .poster {
    position: absolute;
    left: 200px;
    top: 34px;
    width: 800px;
    height: 1080px;
    background: linear-gradient(180deg, var(--poster-top), var(--poster-bottom));
    overflow: hidden;
  }
  .title {
    position: absolute;
    top: 70px;
    left: 0;
    width: 100%;
    text-align: center;
    font-family: "Yellowtail", cursive;
    font-weight: 400;
    color: var(--title);
    line-height: 0.92;
  }
  .title__main {
    display: block;
    font-size: 156px;
  }
  .title__sub {
    display: block;
    margin-top: 4px;
    font-size: 34px;
    color: var(--credit);
  }
  .credits {
    position: absolute;
    top: 408px;
    left: 0;
    width: 640px;
    text-align: center;
    font-family: "Oswald", sans-serif;
    font-weight: 300;
    text-transform: uppercase;
    color: var(--credit);
    line-height: 1.55;
  }
  .credits__line { font-size: 11px; letter-spacing: 0.02em; }
  .credits__name { font-size: 15px; font-weight: 400; color: var(--credit-name); }
  .cast {
    position: absolute;
    left: 56px;
    bottom: 30px;
    display: flex;
    align-items: flex-end;
    gap: 12px;
  }
  .cast__column {
    display: flex;
    flex-direction: column;
    gap: 12px;
  }
  .cast__block {
    width: 88px;
    height: 88px;
    background: var(--tone);
  }
  .cast__portrait { background: var(--tone); }
  .cast__column--coral { --tone: var(--coral); }
  .cast__column--yellow { --tone: var(--yellow); }
  .cast__column--orange { --tone: var(--orange); }
  .cast__column--magenta { --tone: var(--magenta); }
  .cast__column--rose { --tone: var(--rose); }
  .cast__column--purple { --tone: var(--purple); }
  .cast__column--green { --tone: var(--green); }
</style>
</head>
<body>
  <main class="poster">
    <h1 class="title">
      <span class="title__main">Steeple<br>Sisters</span>
      <span class="title__sub">the Musical</span>
    </h1>

    <div class="credits">
      <p class="credits__line">Book and story by <span class="credits__name">Hal Brody</span> music by <span class="credits__name">Toby Kessler,</span> lyrics by <span class="credits__name">Marla Brody</span></p>
      <p class="credits__line">Additional material by <span class="credits__name">Fenwick Ashby</span></p>
    </div>

    <section class="cast" aria-label="Cast of seven">
      <div class="cast__column cast__column--coral">
        <div class="cast__block cast__portrait" role="img" aria-label="Silhouette of a cast member's hairdo"></div>
        <div class="cast__block"></div>
        <div class="cast__block"></div>
      </div>
      <div class="cast__column cast__column--yellow">
        <div class="cast__block cast__portrait" role="img" aria-label="Silhouette of a cast member's hairdo"></div>
        <div class="cast__block"></div>
        <div class="cast__block"></div>
        <div class="cast__block"></div>
      </div>
      <div class="cast__column cast__column--orange">
        <div class="cast__block cast__portrait" role="img" aria-label="Silhouette of a cast member's bob haircut"></div>
        <div class="cast__block"></div>
        <div class="cast__block"></div>
        <div class="cast__block"></div>
        <div class="cast__block"></div>
      </div>
      <div class="cast__column cast__column--magenta">
        <div class="cast__block cast__portrait" role="img" aria-label="Silhouette of a cast member with curls and cat-eye glasses"></div>
        <div class="cast__block"></div>
      </div>
      <div class="cast__column cast__column--rose">
        <div class="cast__block cast__portrait" role="img" aria-label="Silhouette of a cast member with curly hair and glasses"></div>
        <div class="cast__block"></div>
        <div class="cast__block"></div>
        <div class="cast__block"></div>
      </div>
      <div class="cast__column cast__column--purple">
        <div class="cast__block cast__portrait" role="img" aria-label="Silhouette of a cast member with a halo and round glasses"></div>
        <div class="cast__block"></div>
        <div class="cast__block"></div>
      </div>
      <div class="cast__column cast__column--green">
        <div class="cast__block cast__portrait" role="img" aria-label="Silhouette of a cast member's shaggy hairdo"></div>
        <div class="cast__block"></div>
        <div class="cast__block"></div>
        <div class="cast__block"></div>
        <div class="cast__block"></div>
        <div class="cast__block"></div>
      </div>
    </section>
  </main>
</body>
</html>
```